Business Card Design

I need a business card design for my law office based in Pasadena, California. I am a sole practitioner and I specialize in business transaction and litigation, probate and estate planning, taxation law, corporate and business formation, immigration and real estate. I want something that is simple, yet stands out.

A friend helped to create a logo about 6 years ago. I am open to new ideas to changing the logo.

Industry/Entity Type

Business

Contact Information for Business Card

Law Offices of Doran M. Vaske
482 W. Harlow Ave., Suite 312
Pasadena, CA 91108
Tel: 626-503-7719
Fax: 626-581-9046
Email: dvaske@dmvlegalgrp.example

Attorney: Doran M. Vaske

```html
<!DOCTYPE html>
<html lang="en">
<head>
<meta charset="utf-8">
<title>Doran M. Vaske – Business Card</title>
<link rel="stylesheet" href="https://fonts.googleapis.com/css2?family=Cinzel:wght@400;500&family=Marcellus&display=swap">
<style>
  :root {
    --backdrop: #3b322e;
    --card-white: #fbfbfa;
    --ink: #111111;
    --card-black: #141414;
    --stripe-grey: #5a5656;
    --soft-grey: #8d8a88;
    --mark-grey: #2b2b2b;
  }
  * { box-sizing: border-box; margin: 0; padding: 0; }
  html, body { width: 1200px; height: 716px; overflow: hidden; }
  body {
    background: var(--backdrop);
    font-family: "Marcellus", serif;
    position: relative;
  }
  .card {
    position: absolute;
    top: 210px;
    width: 520px;
    height: 297px;
    overflow: hidden;
    box-shadow: 0 10px 24px rgba(0,0,0,.35);
  }
  /* Back side */
  .card-back { left: 50px; background: var(--card-black); }
  .back-mark {
    position: absolute; left: 50%; top: 50%;
    transform: translate(-50%, -50%);
    display: flex; align-items: center; gap: 14px;
  }
  .back-mark .mark-square { width: 26px; height: 26px; background: var(--mark-grey); }
  .back-mark .mark-name {
    font-family: "Cinzel", serif; font-size: 22px; letter-spacing: 2px;
    color: var(--mark-grey);
  }
  /* Front side */
  .card-front { left: 630px; background: var(--card-white); color: var(--ink); }
  .front-waves { position: absolute; inset: 0; }
  .brand { position: absolute; left: 34px; top: 34px; width: 230px; text-align: center; }
  .brand-mark { display: flex; align-items: center; justify-content: center; gap: 10px; margin-bottom: 16px; }
  .brand-mark .mark-square { width: 22px; height: 22px; background: var(--ink); }
  .brand-mark .mark-name { font-family: "Cinzel", serif; font-size: 15px; letter-spacing: 1.5px; color: var(--ink); }
  .firm-label {
    font-family: "Cinzel", serif; font-size: 8px; letter-spacing: 4px;
    color: var(--soft-grey); text-transform: uppercase;
  }
  .firm-name {
    font-family: "Cinzel", serif; font-size: 24px; letter-spacing: .5px;
    border-top: 1px solid var(--soft-grey); padding-top: 4px; margin-top: 3px;
    border-bottom: 1px solid var(--soft-grey); padding-bottom: 2px;
    white-space: nowrap;
  }
  .contact {
    position: absolute; right: 20px; top: 44px;
    list-style: none; text-align: right;
    font-family: "Marcellus", serif; font-size: 11px; line-height: 15px; letter-spacing: .6px;
    text-transform: uppercase;
  }
  .contact li { display: flex; justify-content: flex-end; align-items: center; gap: 8px; }
  .contact svg { width: 9px; height: 9px; fill: var(--ink); flex: none; }
  .contact .no-icon { padding-right: 17px; }
  .signature {
    position: absolute; right: 34px; bottom: 18px; text-align: right; color: #fff;
  }
  .signature-name { font-family: "Cinzel", serif; font-size: 20px; letter-spacing: .5px; line-height: 24px; }
  .signature-title { font-family: "Marcellus", serif; font-size: 12px; letter-spacing: .8px; margin-top: 2px; }
</style>
</head>
<body>
  <section class="card card-back" aria-label="Card back">
    <div class="back-mark">
      <span class="mark-square"></span>
      <span class="mark-name">Vaske Law</span>
    </div>
  </section>

  <section class="card card-front" aria-label="Card front">
    <svg class="front-waves" viewBox="0 0 520 297" aria-hidden="true">
      <path d="M0,168 C100,218 230,226 330,192 C410,165 465,150 520,142" stroke="var(--stripe-grey)" stroke-width="1.5" fill="none"/>
      <path d="M0,182 C110,238 240,242 340,204 C420,174 470,160 520,152 L520,161 C470,169 420,183 340,213 C240,251 110,248 0,192 Z" fill="var(--stripe-grey)"/>
      <path d="M0,205 C110,262 240,262 340,222 C420,192 470,178 520,170 L520,297 L0,297 Z" fill="var(--card-black)"/>
    </svg>

    <div class="brand">
      <div class="brand-mark">
        <span class="mark-square"></span>
        <span class="mark-name">Vaske Law</span>
      </div>
      <div class="firm-label">Law Offices of</div>
      <div class="firm-name">Doran M. Vaske</div>
    </div>

    <ul class="contact">
      <li class="no-icon">626-503-7719</li>
      <li>626-581-9046
        <svg viewBox="0 0 10 10"><path d="M2 0.5h2l.7 2.3-1.2.9a5 5 0 0 0 2.8 2.8l.9-1.2 2.3.7v2a1 1 0 0 1-1 1A8.5 8.5 0 0 1 1 1.5a1 1 0 0 1 1-1z"/></svg></li>
      <li>dvaske@dmvlegalgrp.example
        <svg viewBox="0 0 10 10"><path d="M2 0h6v3H2zM0 3.5h10v4.5H8V10H2V8H0zM3 7h4v2H3z"/></svg></li>
      <li>482 W. Harlow Ave., Suite 312
        <svg viewBox="0 0 10 10"><path d="M0 1.5h10v7H0zM.8 2.3 5 5.5l4.2-3.2v.9L5 6.4.8 3.2z" fill-rule="evenodd"/></svg></li>
      <li>Pasadena, CA 91108
        <svg viewBox="0 0 10 10"><path d="M5 0a3.5 3.5 0 0 1 3.5 3.5C8.5 6 5 10 5 10S1.5 6 1.5 3.5A3.5 3.5 0 0 1 5 0zm0 2a1.4 1.4 0 1 0 0 2.8A1.4 1.4 0 0 0 5 2z"/></svg></li>
    </ul>

    <div class="signature">
      <div class="signature-name">Doran M. Vaske</div>
      <div class="signature-title">Attorney</div>
    </div>
  </section>
</body>
</html>
```